KVT Business Cards

We require business cards for our business. We would like a matte black back to the card, with our logo centred in the middle. The front side of the card is open to design.

Target Market(s)

Clients looking for legal services (professional)

Industry/Entity Type

Legal

Contact Information for Business Card

Boris Telemark
Partner
Mobile: 0438 715 642
Email: boris@kvtlaw.co
Website: www.kvtlaw.co
Level 3, 118 Wexbury Street
Sydney NSW 2000

Font styles to use
Other font styles liked:
• Avenir

Colors
f04a50
ffffff
1b1b1b

Requirements
Must have
• Black back with logo included in the centre of the card.
• Our font is Avenir.

```html
<!DOCTYPE html>
<html lang="en">
<head>
<meta charset="utf-8">
<title>KVT Legal – Business Cards</title>
<link rel="stylesheet" href="https://fonts.googleapis.com/css2?family=Roboto:wght@500;700&family=Nunito+Sans:wght@400&display=swap">
<style>
  :root {
    --ink: #121516;
    --paper: #ffffff;
    --accent: #f0294f;
    --text-dark: #111111;
    --text-light: #ffffff;
  }
  * { margin: 0; padding: 0; box-sizing: border-box; }
  html, body {
    width: 1200px; height: 1200px; overflow: hidden;
    background: var(--paper);
  }
  .sheet { position: relative; width: 1200px; height: 1200px; }

  .card {
    position: absolute; left: 205px; width: 840px; height: 480px; overflow: hidden;
  }
  .card--front { top: 92px; background: var(--paper); }
  .card--back  { top: 635px; background: var(--ink); }

  .front-panel { position: absolute; inset: 0; }

  .brand {
    position: absolute; display: flex; align-items: center; gap: 22px;
  }
  .brand__mark { width: 46px; height: 46px; background: var(--accent); flex: none; }
  .brand__name {
    font-family: "Roboto", sans-serif; font-weight: 700;
    line-height: 1.02; letter-spacing: 0.5px;
  }
  .card--front .brand { left: 120px; top: 62px; }
  .card--front .brand__name { font-size: 38px; color: var(--text-dark); }
  .card--back .brand { left: 50%; top: 50%; transform: translate(-50%, -50%); }
  .card--back .brand__mark { width: 58px; height: 58px; }
  .card--back .brand__name { font-size: 46px; color: var(--text-light); }

  .person { position: absolute; left: 601px; top: 56px; }
  .person__name {
    font-family: "Roboto", sans-serif; font-weight: 500;
    font-size: 35px; color: var(--text-light); letter-spacing: 0.5px; line-height: 1.1;
  }
  .person__role {
    font-family: "Roboto", sans-serif; font-weight: 500;
    font-size: 22px; color: var(--accent); margin-top: 2px; letter-spacing: 0.3px;
  }

  .contact-icon {
    position: absolute; width: 60px; height: 60px; border-radius: 50%;
    background: var(--accent); display: flex; align-items: center; justify-content: center;
  }
  .contact-icon svg { width: 32px; height: 32px; }
  .contact-text {
    position: absolute; font-family: "Nunito Sans", sans-serif; font-weight: 400;
    font-size: 22px; color: var(--text-light); line-height: 28px; transform: translateY(-50%);
    white-space: nowrap;
  }
  .contact-text--address { transform: none; }
</style>
</head>
<body>
<main class="sheet">

  <section class="card card--front" aria-label="Front of card">
    <svg class="front-panel" viewBox="0 0 840 480" preserveAspectRatio="none" aria-hidden="true">
      <polygon points="595,0 116,480 840,480 840,0" fill="var(--ink)"/>
    </svg>

    <div class="brand">
      <span class="brand__mark" aria-hidden="true"></span>
      <p class="brand__name">KVT<br>LEGAL</p>
    </div>

    <div class="person">
      <p class="person__name">BORIS TELEMARK</p>
      <p class="person__role">PARTNER</p>
    </div>

    <span class="contact-icon" style="left:396px;top:198px" aria-hidden="true">
      <svg viewBox="0 0 32 32" fill="none" stroke="#fff" stroke-width="2.4" stroke-linecap="round">
        <circle cx="16" cy="16" r="13"/>
        <path d="M11 9.5l2.5-1 2 4-1.8 1.3c.8 2 2.3 3.5 4.3 4.3l1.3-1.8 4 2-1 2.5c-6 .5-11.8-5.3-11.3-11.3z" fill="#fff" stroke-width="1.2"/>
      </svg>
    </span>
    <p class="contact-text" style="left:472px;top:228px">0438 715 642</p>

    <span class="contact-icon" style="left:340px;top:254px" aria-hidden="true">
      <svg viewBox="0 0 32 32">
        <rect x="4" y="7" width="24" height="18" rx="3" fill="#fff"/>
        <path d="M5 9l11 8 11-8" fill="none" stroke="var(--accent)" stroke-width="2.2"/>
      </svg>
    </span>
    <p class="contact-text" style="left:416px;top:284px">boris@kvtlaw.co</p>

    <span class="contact-icon" style="left:284px;top:310px" aria-hidden="true">
      <svg viewBox="0 0 32 32" fill="none" stroke="#fff" stroke-width="2">
        <circle cx="16" cy="16" r="12"/>
        <ellipse cx="16" cy="16" rx="5.5" ry="12"/>
        <path d="M4 16h24M6 10h20M6 22h20M16 4v24"/>
      </svg>
    </span>
    <p class="contact-text" style="left:359px;top:340px">www.kvtlaw.co</p>

    <span class="contact-icon" style="left:229px;top:366px" aria-hidden="true">
      <svg viewBox="0 0 32 32">
        <path d="M16 5L3 16.5h4V27h7v-7h4v7h7V16.5h4z" fill="#fff"/>
      </svg>
    </span>
    <p class="contact-text contact-text--address" style="left:346px;top:387px">Level 3, 118 Wexbury Street,<br>Sydney NSW 2000</p>
  </section>

  <section class="card card--back" aria-label="Back of card">
    <div class="brand">
      <span class="brand__mark" aria-hidden="true"></span>
      <p class="brand__name">KVT<br>LEGAL</p>
    </div>
  </section>

</main>
</body>
</html>
```